Mobile Repair Service on location needs a Web Design

We are starting a new mobile device repair service called Gadget Haven and our website needs a design!

Hello Designers!
First, we'd like to make clear this is more than a simple web design contest, we want the designers to create an idea. We want someone who can create the whole theme of the service's we provide. We want someone that can help design our visual branding, help us communicate a sentiment. And we are willing to pay for that.

Who are we?
Our company is based in Rotterdam, the Netherlands. We provide different services for all kinds of electronic devices. The kind of services we provide are, among other things, installations of hardware and software and the repair of broken or malfunctioning devices.
We are starting a new service that offers mobile device repairs on location, be it at the home of our customers, their office, or any other place. Just give us the address and we will come to you for the repair job. This is also our main USP. We have multiple skilled engineers who drive trough the country on a daily basis and can be on location within a working day. Repair is done immediately onsite while the customer waits. At this stage we will start with the smartphone product-group within the mobile devices. In a second phase we might also add tablets.
People don't want to be without their phone for weeks because of some parts that needed to be ordered by a repair center they had to sent their phone to. We offer a fully functional mobile repair center in the form of specially customized vans. These vans have all the tools and utilities needed by our engineers to safely repair your mobile device. Your phone is being repaired directly in front of you, the next business-day, on a location you desire.

For this new service we are creating a website called Gadget Haven. The website needs a story and matching design and this is where you come in. We are not looking for a simple template design we can get from any place. We need a story. We want you to create an idea, build a unique theme or vision that helps sell the product/service. This goes beyond the design of the website. We need the whole package, the design you are creating needs to have returning elements like icons, color use, images, maybe even characters etc. You name it! There needs to be a common thread in the design so we can reuse elements in, for example, the email templates, the work order or receipt we give to our customers (we may contact the winner of the contest to design these for us as well!).

The name 'Gadget Haven' is chosen. Haven (short for rehabilitate) has a bold and playful tone to it and the design needs to reflect the name. So we're looking for a somewhat playful and cheeky design. Definitely not too serious and definitely modern. We already got a logo that we love and that fit's this description (see attached design documents for the logo). It's bold, powerful and fun. Our web design needs to reflect this as well and has to fit in with our logo.
We would really like it if the design somehow incorporates elements that highlight our unique selling points (repairs on location, we come to you etc.). We would really like some form of story telling in the design. Think clumsy people breaking their phones. Teenagers in tears because they have no access to their friends. People nowadays have the need to always be 'connected'. What happens when your phone is broken or malfunctioning? We're handling tech, we are nerds and a little bit weird, but we're professionals and here to help you with your problem. The sentiment Wire Troop tries to communicate is something we really like. We're looking for fresh idea's, anything goes!

In an overview all Unique Selling Points of the Gadget haven service:
- Professional service on location. Don’t ship to us we will come to you!
- Clear pricing upfront. No hidden cost.
- Next business-day repair.
- Backed by a professional call center open 12 hours a day and open on a Saturday as well
- Backed by a professional repair center with more then 12 years of experience
- Repair is done by certified engineers
- 1 year warranty on the repair

The process:
The main function of our website will be for customers to make a repair request. A customer will visit our website and can make a repair request immediately by going through a 'request-order-flow'. In this flow he or she will need to fill in some forms and can select wich type/model/brand of mobile device he or she has and what parts need to be repaired. After a request is placed we will call the customer back (within an hour) for a short intake and to set a date/time and location. Our engineer will meet the customer at the specified location and will repair the device onsite in one of our mobile repair centers, which is a specialized van equipped with all the tools needed for device restorations.
So in short the steps are:
- Choose your device and repair job
- Place the order
- Get a callback within the hour
- Set date and location
- We will come to you.

Website functionality:
Our website is our main form of communication. So the sentiment we want to communicate needs be reflected in the design. We need a main/front page designed (preferably a long scrolling page design) containing:
1. Customers will be able to request a repair job directly on our website. So there will need to be a prominent button/link at the top of our main page that will bring the customer to this 'request-order-flow'. This is the main flow which needs to be full focus on the front page. All other items are secondary.
2. The general information of who we are and what we do, and why the customer should choose us. Preferably in short bullet-point type keywords/sentences with icons or other visual cues. See our unique selling points to get an idea of the information that will be displayed here.
3. There needs to be a section that will explain the process (see above) of a repair request step-by- step, again in brief short key sentences and with (custom) icons.
4. There needs to be a section that explains to the customer he/she can always contact us if they are not sure what the problem is with their device, and for this reason are not sure what repair request they should order.
5. We want to implement some functionality that display customer ratings or customer reviews. So there needs to be room for some kind of widget of plugin we're going to implement which shows these reviews.
6. A 'For business section' where we will explain all the options we provide for corporate clients.
7. Social media links.
8. There needs to be a menu with buttons that leads to the all sections described in the previous points.

For now, we need a design for our front page. In the second phase, when we have picked our winner, we may ask the winner to design the page(s) for our request workflow as well.

EDIT:
Finally, we have a very specific order in mind for the different segments of our website. We would like you to add some more segments that were not in our original brief as well:

1. Top header with order/request button. (should instantly make clear our main USP, we do repairs on location)
2. Our process
3. Our unique selling points / why choose us
4. The kind of repairs we do (broken screens, broken batteries, water damage, broken camera's, no sound etc.)
5. A 'meet our team' section, where we introduce some of our engineers
6. A 'contact us for any questions' section/
7. Testimonials/user reviews
8. A section where we show key performance indicators
9. 'For businesses' sections
10.'Subscribe for newsletter' field
11. Social media buttons

Industry/Entity Type

It Service

Number of Pages Required

1 page

Font styles to use
Sans Serif

Requirements
Must have
• a main/front page, design only
• custom icons/images for banners, adverts online and in print (high res)
Nice to have
• Storytelling in our design.
• Design that fits with our brand new logo.
• Elements like icons to have a flat design.
• Keep in mind that the website will need to be responsive when designing! (Ideally provide an example of the mobile design as well)
• Create a fun and trustworthy feeling.

```html
<!DOCTYPE html>
<html lang="en">
<head>
<meta charset="utf-8">
<title>Gadget Haven – Mobile Repair On Location</title>
<link href="https://fonts.googleapis.com/css2?family=Oswald:wght@400;500;700&family=Open+Sans:wght@400;600;700&display=swap" rel="stylesheet">
<style>
:root{
  --orange:#f26522;
  --orange-dark:#d9531a;
  --ink:#2b2b2b;
  --charcoal:#3b3b3b;
  --text:#555;
  --muted:#8a8a8a;
  --cream:#fdf1d8;
  --light:#f4f4f4;
  --white:#fff;
}
*{box-sizing:border-box;margin:0;padding:0}
html,body{width:1200px;height:3804px;overflow:hidden}
body{font-family:"Open Sans",Arial,sans-serif;color:var(--text);background:var(--white);font-size:14px;line-height:1.6}
h1,h2,h3,.nav a,.btn{font-family:Oswald,"Arial Narrow",sans-serif;text-transform:uppercase}
.btn{display:inline-block;background:var(--orange);color:var(--white);font-weight:500;letter-spacing:.5px;border-radius:3px;padding:8px 18px;font-size:13px;text-decoration:none}
.section-title{text-align:center;font-size:26px;color:var(--ink);font-weight:700;position:relative;padding-bottom:14px}
.section-title::after{content:"";position:absolute;left:50%;bottom:0;width:40px;height:3px;background:var(--orange);transform:translateX(-50%)}
.ph{display:block}

/* header */
.hero{position:relative;height:600px;background:linear-gradient(110deg,#1c1c1c 0%,#3a3d42 45%,#5b5e63 70%,#2a2a2c 100%);overflow:hidden}
.topbar{position:absolute;top:0;left:0;right:0;height:80px;display:flex;align-items:center;padding:0 160px;justify-content:space-between;z-index:2}
.brand{display:flex;align-items:center;gap:10px;color:var(--white);font-family:Oswald,sans-serif;font-weight:700;font-size:22px;text-transform:uppercase;line-height:1}
.brand-dot{width:34px;height:34px;border-radius:50%;background:var(--orange)}
.nav{display:flex;align-items:center;gap:26px}
.nav a{color:var(--white);text-decoration:none;font-size:14px;letter-spacing:.5px}
.hero-copy{position:absolute;left:160px;top:250px;z-index:2}
.hero-copy .kicker{color:var(--white);font-size:38px;font-weight:500;letter-spacing:2px;line-height:1}
.hero-copy h1{color:var(--white);font-size:76px;font-weight:700;line-height:1.05;letter-spacing:1px}
.hero-copy .strap{display:inline-block;background:rgba(0,0,0,.55);color:var(--orange);font-family:Oswald,sans-serif;font-size:26px;font-weight:500;padding:2px 12px;text-transform:uppercase}
.hero-photo{position:absolute;right:0;top:0;width:620px;height:600px;background:radial-gradient(ellipse at 55% 40%,#8a8f96 0%,#55585d 45%,transparent 75%)}
.dots{position:absolute;left:50%;bottom:44px;transform:translateX(-50%);display:flex;gap:8px}
.dots span{width:10px;height:10px;border-radius:50%;background:rgba(255,255,255,.5)}
.dots span:first-child{background:var(--orange)}

/* about */
.about{height:740px;position:relative;padding:40px 160px 0}
.about-text{width:400px}
.about h2{font-size:24px;color:var(--ink);font-weight:700;padding-bottom:10px;position:relative;margin-bottom:18px}
.about h2::after{content:"";position:absolute;left:0;bottom:0;width:40px;height:3px;background:var(--orange)}
.about p{font-size:13px;margin-bottom:16px}
.about .what{margin-top:34px}
.ticks{list-style:none}
.ticks li{font-size:13px;padding-left:24px;position:relative;margin-bottom:6px}
.ticks svg{position:absolute;left:0;top:4px}
.about-photo{position:absolute;left:600px;top:40px;width:440px;height:640px;background:linear-gradient(180deg,#e9ecef 0%,#cfd4da 55%,#f5f5f5 100%)}

/* why */
.why{height:640px;display:flex}
.why-photo{width:480px;height:100%;position:relative;background:linear-gradient(160deg,#7d8a99 0%,#4d5b6b 55%,#2e3a48 100%)}
.why-badge{position:absolute;right:-46px;top:262px;width:92px;height:92px;border-radius:50%;background:var(--white);border:6px solid var(--orange);z-index:2}
.why-panel{flex:1;background:var(--orange);padding:40px 70px 0 100px;color:var(--white)}
.why-panel h2{text-align:center;font-size:22px;font-weight:500;letter-spacing:.5px}
.why-grid{display:grid;grid-template-columns:repeat(4,1fr);gap:40px 20px;margin-top:50px}
.why-item{text-align:center;font-size:12px;line-height:1.45}
.why-item .ic{width:76px;height:76px;border-radius:50%;background:var(--ink);border:3px solid var(--white);margin:0 auto 14px;display:flex;align-items:center;justify-content:center}
.why-item b{font-weight:700}

/* process */
.process{height:270px;padding-top:28px}
.steps{display:flex;justify-content:center;gap:46px;margin-top:36px;position:relative}
.step{width:130px;text-align:center;font-size:12px;color:var(--ink);position:relative}
.step .circle{width:78px;height:78px;border-radius:50%;border:3px solid var(--orange);margin:0 auto 12px;display:flex;align-items:center;justify-content:center;background:var(--white);position:relative;z-index:1}
.step:not(:last-child)::after{content:"";position:absolute;top:39px;left:104px;width:122px;border-top:2px dashed #d0d0d0}

/* request */
.request{height:330px;background:var(--cream);position:relative;padding:40px 160px 0}
.request-art{position:absolute;left:160px;top:30px;width:280px;height:280px;background:radial-gradient(circle at 50% 55%,#f5c66c 0%,#f1a955 40%,transparent 72%)}
.request-form{position:absolute;left:470px;top:44px;width:570px}
.request-form h3{font-size:22px;color:var(--ink);font-weight:500;display:flex;align-items:center;gap:8px;margin-bottom:18px}
.field{background:var(--white);border:1px solid #e2d6bf;height:40px;border-radius:3px;font-size:12px;color:var(--muted);padding:0 14px;display:flex;align-items:center;justify-content:space-between}
.row{display:flex;gap:10px;margin-top:12px}
.row .field{flex:1}
.row .field.small{flex:0 0 70px}
.request-form .btn{display:block;text-align:center;margin-top:14px;padding:11px;font-size:15px}

/* reviews */
.reviews{height:420px;background:var(--charcoal);position:relative;padding-top:36px}
.reviews .section-title{color:var(--white);font-size:22px}
.review-cards{display:flex;gap:40px;justify-content:center;margin-top:40px}
.card{width:400px;background:var(--white);border-radius:3px;padding:22px 26px;position:relative}
.card .stars{position:absolute;right:22px;top:14px;display:flex;gap:2px}
.card .quote{font-family:Oswald,sans-serif;font-size:44px;line-height:.6;color:var(--ink);text-align:center}
.card p{font-size:12px;margin-top:10px}
.who{display:flex;align-items:center;gap:12px;margin-top:16px}
.avatar{width:48px;height:48px;border-radius:50%;background:linear-gradient(135deg,#c9b8a6,#8c7a68)}
.who strong{display:block;font-size:13px;color:var(--ink)}
.who span{font-size:11px;color:var(--muted)}
.wave{position:absolute;left:0;bottom:-1px;width:1200px;height:90px}

/* corporate */
.corporate{height:540px;padding-top:30px}
.corp-cards{display:flex;gap:30px;justify-content:center;margin-top:40px}
.corp{width:270px}
.corp .img{height:180px}
.corp h3{font-family:"Open Sans",sans-serif;text-transform:none;font-size:16px;font-weight:700;color:var(--ink);line-height:1.3;margin:16px 0 8px}
.corp p{font-size:12px;margin-bottom:14px}
.corp .btn{padding:5px 14px;font-size:12px}

/* footer */
.footer{height:264px;background:var(--ink);position:relative;padding:44px 160px 0;color:#bdbdbd;font-size:12px}
.to-top{position:absolute;left:50%;top:-22px;transform:translateX(-50%);width:44px;height:44px;border-radius:50%;background:var(--ink);display:flex;align-items:center;justify-content:center}
.foot-cols{display:flex;gap:50px}
.foot-brand{width:250px}
.foot-brand .brand{margin-bottom:18px}
.foot-col h4{font-family:Oswald,sans-serif;text-transform:uppercase;color:var(--white);font-size:14px;font-weight:500;margin-bottom:12px}
.foot-col ul{list-style:none;line-height:1.9}
.foot-col.links{width:110px}
.foot-col.contact{width:170px}
.foot-col.news{width:260px}
.subscribe{display:flex;margin-top:12px}
.subscribe .input{flex:1;background:var(--white);height:34px;border-radius:3px 0 0 3px;color:var(--muted);font-size:11px;padding:0 10px;display:flex;align-items:center}
.subscribe .btn{border-radius:0 3px 3px 0;padding:0 14px;line-height:34px;font-size:12px}
.copy{position:absolute;left:160px;bottom:24px;font-size:11px;color:var(--muted)}
</style>
</head>
<body>

<header class="hero">
  <div class="hero-photo ph" role="img" aria-label="Photo of a smiling repair engineer in work clothes"></div>
  <div class="topbar">
    <div class="brand"><span class="brand-dot"></span>Gadget Haven</div>
    <nav class="nav">
      <a href="#">Home</a><a href="#">About Us</a><a href="#">Services</a><a href="#">Contact Us</a>
      <a class="btn" href="#">Request Order Flow</a>
    </nav>
  </div>
  <div class="hero-copy">
    <div class="kicker">Professional Service</div>
    <h1>On Location.</h1>
    <div class="strap">Don't ship to us we will come to you!</div>
  </div>
  <div class="dots"><span></span><span></span><span></span></div>
</header>

<section class="about">
  <div class="about-text">
    <h2>Who We Are</h2>
    <p>We are a team of friendly tech nerds who fix broken phones where you are. Our engineers travel the country every day in vans fitted out as complete repair workshops.</p>
    <p>Your device is repaired right in front of you, usually the next business day, at home, at work or anywhere you like. No shipping, no long waits, no weeks without your phone.</p>
    <div class="what">
      <h2>What We Do</h2>
      <p>We replace screens, batteries, cameras and more, install hardware and software, and bring dead devices back to life on the spot.</p>
      <ul class="ticks">
        <li><svg width="14" height="12" viewBox="0 0 14 12"><path d="M1 6l4 4 8-9" fill="none" stroke="#f26522" stroke-width="2.4"/></svg>Broken screen replacement on site</li>
        <li><svg width="14" height="12" viewBox="0 0 14 12"><path d="M1 6l4 4 8-9" fill="none" stroke="#f26522" stroke-width="2.4"/></svg>Battery swaps for worn out phones</li>
        <li><svg width="14" height="12" viewBox="0 0 14 12"><path d="M1 6l4 4 8-9" fill="none" stroke="#f26522" stroke-width="2.4"/></svg>Water damage checks and repair</li>
        <li><svg width="14" height="12" viewBox="0 0 14 12"><path d="M1 6l4 4 8-9" fill="none" stroke="#f26522" stroke-width="2.4"/></svg>Camera and sound fixes while you wait</li>
        <li><svg width="14" height="12" viewBox="0 0 14 12"><path d="M1 6l4 4 8-9" fill="none" stroke="#f26522" stroke-width="2.4"/></svg>Software setup and data rescue</li>
      </ul>
    </div>
  </div>
  <div class="about-photo ph" role="img" aria-label="Photo of an engineer with a tablet standing beside a white branded service van"></div>
</section>

<section class="why">
  <div class="why-photo ph" role="img" aria-label="Photo of a smiling engineer holding a tablet">
    <span class="why-badge"></span>
  </div>
  <div class="why-panel">
    <h2>Why the customer should choose us</h2>
    <div class="why-grid">
      <div class="why-item"><div class="ic"><svg width="34" height="34" viewBox="0 0 24 24" fill="none" stroke="#fff" stroke-width="1.8"><path d="M12 22s7-7 7-12a7 7 0 0 0-14 0c0 5 7 12 7 12z"/><circle cx="12" cy="10" r="2.5"/></svg></div><b>Professional service on location.</b> Don't ship to us we will come to you</div>
      <div class="why-item"><div class="ic"><svg width="34" height="34" viewBox="0 0 24 24" fill="none" stroke="#fff" stroke-width="1.8"><path d="M3 12l9-9h8v8l-9 9z"/><circle cx="16" cy="8" r="1.5"/></svg></div><b>Clear pricing upfront.</b> No hidden cost</div>
      <div class="why-item"><div class="ic"><svg width="34" height="34" viewBox="0 0 24 24" fill="none" stroke="#fff" stroke-width="1.8"><rect x="3" y="5" width="18" height="16" rx="2"/><path d="M3 10h18M8 3v4M16 3v4"/></svg></div><b>Next business-day</b> repair</div>
      <div></div>
      <div class="why-item"><div class="ic"><svg width="34" height="34" viewBox="0 0 24 24" fill="none" stroke="#fff" stroke-width="1.8"><circle cx="12" cy="9" r="6"/><path d="M8 14l-2 8 6-3 6 3-2-8"/></svg></div><b>Repair is done by</b> certified engineers</div>
      <div class="why-item"><div class="ic"><svg width="34" height="34" viewBox="0 0 24 24" fill="none" stroke="#fff" stroke-width="1.8"><path d="M12 2l8 4v6c0 5-4 9-8 10-4-1-8-5-8-10V6z"/><path d="M8 12l3 3 5-6"/></svg></div><b>1 year warranty</b> on the repair</div>
      <div class="why-item"><div class="ic"><svg width="34" height="34" viewBox="0 0 24 24" fill="none" stroke="#fff" stroke-width="1.8"><path d="M14 4l6 6-9 9-6-6z"/><path d="M3 21l3-3"/></svg></div><b>Backed by a professional repair center</b> with more than 12 years of experience</div>
      <div class="why-item"><div class="ic"><svg width="34" height="34" viewBox="0 0 24 24" fill="none" stroke="#fff" stroke-width="1.8"><path d="M4 14v-2a8 8 0 0 1 16 0v2"/><rect x="3" y="14" width="4" height="6" rx="1"/><rect x="17" y="14" width="4" height="6" rx="1"/></svg></div><b>Backed by a professional call center</b> open 12 hours a day and open on a Saturday as well</div>
    </div>
  </div>
</section>

<section class="process">
  <h2 class="section-title">The Process</h2>
  <div class="steps">
    <div class="step"><div class="circle"><svg width="32" height="32" viewBox="0 0 24 24" fill="none" stroke="#f26522" stroke-width="1.8"><rect x="6" y="2" width="12" height="20" rx="2"/><path d="M11 18h2"/></svg></div>Choose your device and repair job</div>
    <div class="step"><div class="circle"><svg width="32" height="32" viewBox="0 0 24 24" fill="none" stroke="#f26522" stroke-width="1.8"><path d="M3 4h3l2 11h11l2-8H7"/><circle cx="9" cy="19" r="1.5"/><circle cx="18" cy="19" r="1.5"/></svg></div>Place the order</div>
    <div class="step"><div class="circle"><svg width="32" height="32" viewBox="0 0 24 24" fill="none" stroke="#f26522" stroke-width="1.8"><path d="M5 3h4l2 5-3 2a11 11 0 0 0 6 6l2-3 5 2v4a2 2 0 0 1-2 2A17 17 0 0 1 3 5a2 2 0 0 1 2-2z"/></svg></div>Get a callback within the hour</div>
    <div class="step"><div class="circle"><svg width="32" height="32" viewBox="0 0 24 24" fill="none" stroke="#f26522" stroke-width="1.8"><rect x="3" y="5" width="18" height="16" rx="2"/><path d="M3 10h18M8 3v4M16 3v4"/></svg></div>Set date and location</div>
    <div class="step"><div class="circle"><svg width="34" height="34" viewBox="0 0 24 24" fill="none" stroke="#f26522" stroke-width="1.8"><path d="M2 7h12v9H2zM14 10h4l3 3v3h-7"/><circle cx="6" cy="17" r="2"/><circle cx="17" cy="17" r="2"/></svg></div>We will come to you</div>
  </div>
</section>

<section class="request">
  <div class="request-art ph" role="img" aria-label="Cartoon of an engineer beside a giant smartphone"></div>
  <div class="request-form">
    <h3><svg width="20" height="22" viewBox="0 0 24 24" fill="#f26522"><path d="M12 22s7-7 7-12a7 7 0 0 0-14 0c0 5 7 12 7 12z"/><circle cx="12" cy="10" r="2.5" fill="#fff"/></svg>A Repair Request</h3>
    <div class="field">What parts needs to be repaired?</div>
    <div class="row">
      <div class="field">Model <span>▾</span></div>
      <div class="field">Brand <span>▾</span></div>
      <div class="field small">Date</div>
      <div class="field small">Time</div>
    </div>
    <a class="btn" href="#">Place the Order</a>
  </div>
</section>

<section class="reviews">
  <h2 class="section-title">What Our Customers Say</h2>
  <div class="review-cards">
    <div class="card">
      <div class="stars"><svg width="70" height="12" viewBox="0 0 70 12" fill="#f26522"><path id="s" d="M6 0l1.8 4 4.2.4-3.2 2.8 1 4.3L6 9.3 2.2 11.5l1-4.3L0 4.4 4.2 4z"/><use href="#s" x="14"/><use href="#s" x="28"/><use href="#s" x="42"/><use href="#s" x="56"/></svg></div>
      <div class="quote">“</div>
      <p>The engineer came to my office the next morning and swapped my cracked screen in twenty minutes. Friendly, fast and exactly the price I was quoted upfront. Highly recommended.</p>
      <div class="who"><div class="avatar ph" role="img" aria-label="Customer portrait"></div><div><strong>Sam Lane</strong><span>Happy customer</span></div></div>
    </div>
    <div class="card">
      <div class="stars"><svg width="70" height="12" viewBox="0 0 70 12" fill="#f26522"><use href="#s"/><use href="#s" x="14"/><use href="#s" x="28"/><use href="#s" x="42"/><use href="#s" x="56"/></svg></div>
      <div class="quote">“</div>
      <p>My phone took a swim and I thought it was gone for good. They showed up at my door, fixed it on the spot and even saved all my photos. No weeks of waiting at all.</p>
      <div class="who"><div class="avatar ph" role="img" aria-label="Customer portrait"></div><div><strong>Kim Ortega</strong><span>Happy customer</span></div></div>
    </div>
  </div>
  <svg class="wave" viewBox="0 0 1200 90" preserveAspectRatio="none">
    <path d="M0 40 C200 90 400 0 600 40 S1000 90 1200 30 L1200 90 L0 90Z" fill="#f26522"/>
    <path d="M0 55 C200 100 400 15 600 55 S1000 100 1200 45 L1200 90 L0 90Z" fill="#fff"/>
  </svg>
</section>

<section class="corporate">
  <h2 class="section-title">We Provide for Corporate Clients</h2>
  <div class="corp-cards">
    <div class="corp">
      <div class="img ph" role="img" aria-label="Photo of hands working on a laptop" style="background:linear-gradient(135deg,#3c4e63,#1f2b38)"></div>
      <h3>Fleet repairs for your whole team, on site.</h3>
      <p>One call covers every phone in your company. We visit your office and fix devices between meetings.</p>
      <a class="btn" href="#">Read More</a>
    </div>
    <div class="corp">
      <div class="img ph" role="img" aria-label="Photo of a support agent wearing a headset" style="background:linear-gradient(135deg,#d9c2a8,#8a6f57)"></div>
      <h3>A dedicated help line for business clients.</h3>
      <p>Your own contact person, priority planning and clear monthly reporting for every repair we do.</p>
      <a class="btn" href="#">Read More</a>
    </div>
    <div class="corp">
      <div class="img ph" role="img" aria-label="Photo of a person with gear graphics" style="background:linear-gradient(135deg,#6f8aa3,#2f4357)"></div>
      <h3>Hardware and software setup for offices.</h3>
      <p>New devices installed, configured and ready to use, so your people can get straight back to work.</p>
      <a class="btn" href="#">Read More</a>
    </div>
  </div>
</section>

<footer class="footer">
  <div class="to-top"><svg width="16" height="10" viewBox="0 0 16 10"><path d="M1 9l7-7 7 7" fill="none" stroke="#fff" stroke-width="2"/></svg></div>
  <div class="foot-cols">
    <div class="foot-brand">
      <div class="brand"><span class="brand-dot"></span>Gadget Haven</div>
      <a class="btn" href="#">Request Order Flow</a>
    </div>
    <div class="foot-col links">
      <h4>Quick Links</h4>
      <ul><li>Home</li><li>About Us</li><li>Services</li><li>Contact Us</li></ul>
    </div>
    <div class="foot-col contact">
      <h4>Contact Us</h4>
      <ul><li>Gadget Haven</li><li>Harbour Lane 12</li><li>Rotterdam</li><li>Phone: (010) 555-0142</li><li>hello@gadgethaven.example</li></ul>
    </div>
    <div class="foot-col news">
      <h4>Newsletter Subscribe</h4>
      <p>Enter your email address below and get the latest news.</p>
      <div class="subscribe"><div class="input">Enter your e-mail</div><a class="btn" href="#">Subscribe</a></div>
    </div>
  </div>
  <div class="copy">© 2017 Gadget Haven</div>
</footer>

</body>
</html>
```